Vitalquorra.com

I need a web design for a Online Wellness Center based in Chicago, IL and it's called "Vitalquorra" We provide Health risk assessment to individuals and interventions. Our portal has a Health Activity tracker where our members record health activities and aerobic miles and biometric data. Our Online wellness center tracks the participant's progress toward health goals and awards points for completed activities.
I started working on this website but the designer was not able to designer a website which describes what we do. I need a fresh look on this project. I need a very attractive, responsive website which says what we do.
These are the things we do.
1. We provide Health Risk Assessments to individuals and Co-operations
2. We Provide Free health screenings to undeserved communities
3. Assist individuals access free or affordable medications
4. We ask providers/doctors to see (or do a complete physical) one individual free of charge once a year (those individuals who are no insured and don't have money to pay from their pocket)
5. Assist patient access lab work at low cost
Our goal is to provide services that will lower the cost of care for our members.

Here is the website: www.vitalquorra.com still underdevelopment. PLEASE DO NOT COPY THIS STYLE OF WEBSITE. IT'S A BAD DESIGN AND THAT IS WHY I'M RE-DESIGNING THE SITE

Target Market(s)

Health individuals between the age of 21 to 65 Plus years old. Insured and uninsured

Industry/Entity Type

Health And Wellness

Coding

Coded - Design and coding required

Number of Pages Required

5+ page

Colors
0292cd

Requirements
Must have
• I'm still working on this websiteHere is the menu: Home, About us, Services, Health Screening, Providers, Contacts
• Please see. www.vitalquorra.com
Nice to have
• Event calender
• Upcoming Event
• Medication
• Lab assist
• Providers/Free Clinics

```html
<!DOCTYPE html>
<html lang="en">
<head>
<meta charset="utf-8">
<title>Vitalquorra – Online Wellness Center</title>
<link href="https://fonts.googleapis.com/css2?family=Open+Sans:wght@400;600;700&family=Roboto:wght@300;400;500;700&display=swap" rel="stylesheet">
<style>
:root{
  --blue:#0292cd;
  --blue-dark:#0a6fa0;
  --green:#8cc63f;
  --green-dark:#6fa92a;
  --ink:#3b3b3b;
  --muted:#8a8a8a;
  --line:#e2e2e2;
  --gray-bg:#efefef;
  --pale-blue:#dff1fa;
  --footer:#2f2f2f;
  --footer-deep:#242424;
  --white:#fff;
}
*{box-sizing:border-box;margin:0;padding:0}
html,body{width:1200px;height:2248px;overflow:hidden}
body{font-family:"Open Sans",Arial,sans-serif;color:var(--ink);background:var(--white);font-size:11px;line-height:1.5}
.wrap{width:780px;margin:0 auto;position:relative}
a{color:inherit;text-decoration:none}

/* header */
.site-header{height:60px}
.site-header .wrap{display:flex;justify-content:space-between;align-items:center;height:60px}
.brand{display:flex;align-items:center;gap:8px;font-family:"Roboto",sans-serif;font-weight:700;font-size:26px;color:var(--blue);letter-spacing:-.5px}
.brand-dot{width:20px;height:20px;border-radius:50%;background:var(--green)}
.header-info{display:flex;align-items:center;gap:16px;font-size:10px;color:var(--muted)}
.header-info .item{display:flex;align-items:center;gap:5px}
.search{width:100px;height:22px;border:1px solid var(--line);font-size:9px;color:var(--muted);padding:4px 6px}

.main-nav{height:22px;background:var(--blue)}
.main-nav ul{list-style:none;display:flex;gap:22px;font-family:"Roboto",sans-serif;font-weight:500;font-size:9.5px;color:var(--white);line-height:22px;letter-spacing:.3px}

/* hero */
.hero{height:288px;background:var(--gray-bg);padding-top:26px}
.hero-card{background:var(--white);display:flex;height:232px;box-shadow:0 1px 3px rgba(0,0,0,.08)}
.hero-photo{width:390px;height:232px;background:linear-gradient(135deg,#cfe6f1,#9cc3d6 55%,#e8eef2)}
.hero-copy{flex:1;padding:28px 30px}
.hero-copy h1{font-family:"Roboto",sans-serif;font-weight:400;font-size:22px;color:var(--ink);line-height:1.2}
.hero-copy h2{font-family:"Roboto",sans-serif;font-weight:500;font-size:15px;color:var(--blue);margin:6px 0 12px}
.hero-copy p{color:var(--muted);font-size:10px}
.hero-actions{display:flex;align-items:center;gap:10px;margin-top:16px}
.btn-line{border:1px solid var(--blue);color:var(--blue);font-size:9.5px;padding:4px 14px}
.dots{display:flex;gap:4px}
.dots span{width:12px;height:12px;border-radius:50%;border:1px solid #bbb}
.dots span.on{background:#bbb}

/* services intro */
.services-intro{height:70px;text-align:center;padding-top:16px}
.section-title{font-family:"Roboto",sans-serif;font-weight:500;font-size:14px;color:var(--ink);letter-spacing:.5px}
.section-title b{color:var(--blue);font-weight:500}
.services-intro p{color:var(--muted);font-size:9px;margin-top:6px;line-height:1.45}

/* service boxes */
.service-row{height:105px;display:grid;grid-template-columns:repeat(4,1fr);gap:4px}
.service{background:var(--green);color:var(--white);text-align:center;padding:10px 12px}
.service svg{width:22px;height:22px}
.service h3{font-family:"Roboto",sans-serif;font-size:12px;font-weight:500;margin:2px 0 3px}
.service p{font-size:8.5px;line-height:1.35;opacity:.95}
.btn-small{display:inline-block;margin-top:6px;font-size:7.5px;padding:2px 8px;background:var(--green-dark);color:var(--white)}

/* events & calendar */
.events-area{height:285px;padding-top:24px}
.events-area .wrap{display:flex;gap:30px}
.events{width:350px}
.schedule{flex:1}
.col-title{font-family:"Roboto",sans-serif;font-weight:500;font-size:12.5px;margin-bottom:10px;display:flex;justify-content:space-between;align-items:center}
.col-title small{font-size:8px;color:#e2513b;font-weight:700}
.event{display:flex;gap:12px;padding:8px 0;border-bottom:1px solid var(--line)}
.event-photo{width:72px;height:60px;background:linear-gradient(135deg,#b9d7e6,#6fa6c3)}
.event h4{font-family:"Roboto",sans-serif;font-weight:400;font-size:13px}
.event .date{display:inline-block;font-size:8px;background:var(--blue);color:var(--white);padding:0 5px;margin:2px 0}
.event p{font-size:8.5px;color:var(--muted);line-height:1.35}
.event .btn-line{font-size:7.5px;padding:1px 8px;display:inline-block;margin-top:4px}
.view-all{text-align:center;font-size:8.5px;font-weight:700;margin-top:10px}
.cal-head{display:flex;align-items:center;gap:6px;margin-bottom:6px}
.cal-head .pill{border:1px solid var(--line);font-size:8px;padding:1px 6px}
.cal-head .month{flex:1;text-align:center;font-weight:600;font-size:10px}
.cal-head .pill.on{background:var(--green);color:var(--white);border-color:var(--green)}
.calendar{width:100%;border-collapse:collapse;font-family:"Roboto",sans-serif}
.calendar th{font-size:10px;font-weight:500;padding:5px 0}
.calendar td{text-align:center;font-size:10.5px;color:#666;height:30px}
.calendar td.today span{display:inline-block;width:22px;height:22px;line-height:20px;border:1px solid var(--ink);border-radius:50%}

/* overview */
.overview{height:315px;background:var(--gray-bg);padding-top:24px;text-align:center}
.tabs{display:flex;justify-content:center;gap:30px;margin:12px 0 16px;font-size:9.5px}
.tabs .on{color:var(--blue)}
.tabs span{color:var(--ink)}
.overview-cols{display:grid;grid-template-columns:1fr 1fr;gap:40px;text-align:left}
.overview-cols h4{font-family:"Roboto",sans-serif;font-weight:500;font-size:11px;margin:6px 0 3px}
.overview-cols p{font-size:8.5px;color:var(--muted);line-height:1.45}
.tag-row{display:flex;gap:6px;flex-wrap:wrap;margin-bottom:8px}
.tag-row span{font-size:7.5px;border:1px solid #c8c8c8;padding:1px 6px;background:var(--white)}

/* checklist */
.checklists{height:305px;background:var(--pale-blue);padding-top:36px}
.checklists .wrap{display:grid;grid-template-columns:1fr 1fr;gap:40px}
.check-box{border:1px dashed #9fcde3;padding:14px 16px;background:#eaf7fd}
.check-box li{list-style:none;display:flex;align-items:center;gap:7px;font-size:8.5px;color:#6a8796;padding:4px 0}
.check-box li i{width:9px;height:9px;border:1px solid var(--blue);display:inline-block;position:relative}

/* clinics map */
.clinics{height:570px;position:relative}
.clinics-map{position:absolute;inset:0;background:linear-gradient(160deg,#dde9d4 0%,#cfe2c2 35%,#e9e4d6 60%,#d5e3ea 100%)}
.clinic-search{position:absolute;left:0;right:0;top:0;height:60px;background:linear-gradient(to bottom,rgba(2,146,205,.85),rgba(2,146,205,.35));}
.clinic-search .wrap{display:flex;align-items:center;gap:12px;height:60px}
.clinic-search h3{font-family:"Roboto",sans-serif;font-weight:500;font-size:13px;color:var(--white);margin:0 auto}
.clinic-search input{width:200px;height:22px;border:none;font-size:9px;padding:0 8px;color:var(--muted)}
.map-pin{position:absolute;left:470px;top:160px}

/* footer */
.site-footer{height:228px;background:var(--footer);color:#cfcfcf}
.footer-top{display:flex;justify-content:space-between;padding-top:24px;height:170px}
.site-footer .brand{color:var(--white);font-size:20px}
.site-footer .brand-dot{width:16px;height:16px}
.footer-copy{font-size:8.5px;color:#999;margin-top:8px}
.footer-contact li{list-style:none;display:flex;align-items:center;gap:6px;font-size:9px;margin-bottom:6px}
.footer-bottom{height:58px;background:var(--footer-deep)}
.footer-bottom ul{list-style:none;display:flex;justify-content:center;gap:22px;font-size:9px;line-height:58px}
</style>
</head>
<body>

<header class="site-header">
  <div class="wrap">
    <div class="brand"><span class="brand-dot"></span>Vitalquorra</div>
    <div class="header-info">
      <div class="item">
        <svg width="10" height="10" viewBox="0 0 24 24"><path fill="#0292cd" d="M6.6 10.8a15 15 0 006.6 6.6l2.2-2.2c.3-.3.7-.4 1-.2 1.1.4 2.3.6 3.6.6.6 0 1 .4 1 1V20c0 .6-.4 1-1 1A17 17 0 013 4c0-.6.4-1 1-1h3.5c.6 0 1 .4 1 1 0 1.3.2 2.5.6 3.6.1.3 0 .7-.2 1z"/></svg>
        (312) 555-0148
      </div>
      <div class="item">
        <svg width="10" height="10" viewBox="0 0 24 24"><path fill="#0292cd" d="M3 5h18v14H3zm2 2v.5l7 4.5 7-4.5V7z"/></svg>
        care@vitalquorra.com
      </div>
      <div class="search">Search</div>
    </div>
  </div>
</header>

<nav class="main-nav">
  <div class="wrap">
    <ul><li>HOME</li><li>ABOUT US</li><li>OUR SERVICES</li><li>HEALTH SCREENING</li><li>PROVIDERS</li><li>CONTACT</li></ul>
  </div>
</nav>

<section class="hero">
  <div class="wrap">
    <div class="hero-card">
      <div class="hero-photo" role="img" aria-label="Photo of a clinician performing a health screening with a patient"></div>
      <div class="hero-copy">
        <h1>Do you know about your risk factor?</h1>
        <h2>We avail Health screening service</h2>
        <p>Free and affordable health screenings help you spot risks early. Our assessments give individuals and companies a clear view of their health so they can act before costs rise.</p>
        <div class="hero-actions">
          <a class="btn-line">Learn more</a>
          <div class="dots"><span class="on"></span><span></span><span></span></div>
        </div>
      </div>
    </div>
  </div>
</section>

<section class="services-intro">
  <div class="wrap">
    <h2 class="section-title">OUR <b>WELLNESS</b> SERVICES</h2>
    <p>Vitalquorra is an online wellness center offering health risk assessments to individuals and corporations. We provide free screenings to underserved communities, help members reach affordable medication and low cost lab work, and connect uninsured people with providers who offer one free physical each year.</p>
  </div>
</section>

<section class="wrap service-row">
  <div class="service">
    <svg viewBox="0 0 24 24"><rect x="3" y="8" width="18" height="8" rx="4" fill="none" stroke="#fff" stroke-width="2"/><line x1="12" y1="8" x2="12" y2="16" stroke="#fff" stroke-width="2"/></svg>
    <h3>Medication</h3>
    <p>We help members find free or affordable medication from trusted programs.</p>
    <a class="btn-small">READ MORE</a>
  </div>
  <div class="service">
    <svg viewBox="0 0 24 24"><path d="M12 21s-8-5-8-11a4 4 0 018-1 4 4 0 018 1c0 6-8 11-8 11z" fill="none" stroke="#fff" stroke-width="2"/></svg>
    <h3>Health Screening</h3>
    <p>Free screenings bring early checks to underserved communities near you.</p>
    <a class="btn-small">READ MORE</a>
  </div>
  <div class="service">
    <svg viewBox="0 0 24 24"><path d="M9 3h6M10 3v6l-5 10h14l-5-10V3" fill="none" stroke="#fff" stroke-width="2"/></svg>
    <h3>Lab Test</h3>
    <p>Access lab work at low cost through our partner labs across the city.</p>
    <a class="btn-small">READ MORE</a>
  </div>
  <div class="service">
    <svg viewBox="0 0 24 24"><polyline points="3,12 8,12 10,6 14,18 16,12 21,12" fill="none" stroke="#fff" stroke-width="2"/></svg>
    <h3>Wellness Process</h3>
    <p>Track activity, goals and points as you build healthier habits each day.</p>
    <a class="btn-small">READ MORE</a>
  </div>
</section>

<section class="events-area">
  <div class="wrap">
    <div class="events">
      <h3 class="col-title">UPCOMING HEALTH SCREENING EVENTS</h3>
      <div class="event">
        <div class="event-photo" role="img" aria-label="Photo from a community health campus event"></div>
        <div>
          <h4>Health Campus</h4>
          <span class="date">12 Sept 2015</span>
          <p>Free blood pressure, glucose and weight checks for all residents at our community campus day.</p>
          <a class="btn-line">CONTINUE READING</a>
        </div>
      </div>
      <div class="event">
        <div class="event-photo" role="img" aria-label="Photo from a community health campus event"></div>
        <div>
          <h4>Health Campus</h4>
          <span class="date">26 Sept 2015</span>
          <p>Meet local providers and get a free risk assessment with results explained on the same day.</p>
          <a class="btn-line">CONTINUE READING</a>
        </div>
      </div>
      <div class="view-all">▸ VIEW ALL EVENTS</div>
    </div>

    <div class="schedule">
      <h3 class="col-title">OUR SCREENING SCHEDULE <small>CREATE NEW EVENT</small></h3>
      <div class="cal-head">
        <span class="pill">‹</span><span class="pill">›</span><span class="pill">Today</span>
        <span class="month">September 2015</span>
        <span class="pill on">Month</span><span class="pill">Week</span><span class="pill">Day</span>
      </div>
      <table class="calendar">
        <tr><th>S</th><th>M</th><th>T</th><th>W</th><th>T</th><th>F</th><th>S</th></tr>
        <tr><td></td><td></td><td>1</td><td>2</td><td>3</td><td>4</td><td>5</td></tr>
        <tr><td>6</td><td>7</td><td>8</td><td class="today"><span>9</span></td><td>10</td><td>11</td><td>12</td></tr>
        <tr><td>13</td><td>14</td><td>15</td><td>16</td><td>17</td><td>18</td><td>19</td></tr>
        <tr><td>20</td><td>21</td><td>22</td><td>23</td><td>24</td><td>25</td><td>26</td></tr>
        <tr><td>27</td><td>28</td><td>29</td><td>30</td><td></td><td></td><td></td></tr>
      </table>
    </div>
  </div>
</section>

<section class="overview">
  <div class="wrap">
    <h2 class="section-title">AN OVER VIEW OF OUR WELLNESS SOLUTIONS</h2>
    <div class="tabs"><span class="on">Our Wellness Solutions</span><span>Measurable Results at an Affordable Price</span></div>
    <div class="overview-cols">
      <div>
        <h4>Health Activity Tracker</h4>
        <p>Members record daily health activities, aerobic miles and biometric data in one simple place. Every entry adds to a clear picture of progress over time.</p>
        <h4>Online wellness center</h4>
        <p>Our center follows each participant toward personal health goals and awards points for completed activities, keeping motivation high all year long.</p>
      </div>
      <div>
        <h4>Personal Wellness Profile</h4>
        <p>Each member receives a profile built from the health risk assessment, with tailored steps and reminders that lower the cost of care.</p>
        <div class="tag-row" style="margin-top:10px"><span>Risk Assessment</span><span>Screenings</span><span>Medication</span><span>Lab Assist</span><span>Free Clinics</span></div>
        <h4>Online wellness center</h4>
        <p>Review results, book screenings and talk with providers from any device, at a time that suits you and your family.</p>
      </div>
    </div>
  </div>
</section>

<section class="checklists">
  <div class="wrap">
    <ul class="check-box">
      <li><i></i>Health risk assessments for individuals</li>
      <li><i></i>Programs for companies and teams</li>
      <li><i></i>Free screenings in local communities</li>
      <li><i></i>Help finding affordable medication</li>
      <li><i></i>Low cost lab work access</li>
      <li><i></i>One free yearly physical for uninsured</li>
    </ul>
    <ul class="check-box">
      <li><i></i>Track aerobic miles and activities</li>
      <li><i></i>Record biometric data securely</li>
      <li><i></i>Earn points for completed goals</li>
      <li><i></i>See progress toward health targets</li>
      <li><i></i>Find providers and free clinics</li>
      <li><i></i>Lower your total cost of care</li>
    </ul>
  </div>
</section>

<section class="clinics">
  <div class="clinics-map" role="img" aria-label="Street map showing nearby providers and free clinics in Chicago"></div>
  <div class="clinic-search">
    <div class="wrap">
      <input value="Enter your zip code" readonly>
      <h3>Providers/Free Clinics</h3>
      <input value="Search by clinic name" readonly>
    </div>
  </div>
  <svg class="map-pin" width="26" height="36" viewBox="0 0 24 34"><path d="M12 0a12 12 0 00-12 12c0 9 12 22 12 22s12-13 12-22A12 12 0 0012 0z" fill="#e2513b"/><circle cx="12" cy="12" r="4.5" fill="#fff"/></svg>
</section>

<footer class="site-footer">
  <div class="wrap footer-top">
    <div>
      <div class="brand"><span class="brand-dot"></span>Vitalquorra</div>
      <p class="footer-copy">© Vitalquorra 2015 . All rights reserved</p>
    </div>
    <ul class="footer-contact">
      <li><svg width="10" height="10" viewBox="0 0 24 24"><path fill="#8cc63f" d="M6.6 10.8a15 15 0 006.6 6.6l2.2-2.2c.3-.3.7-.4 1-.2 1.1.4 2.3.6 3.6.6.6 0 1 .4 1 1V20c0 .6-.4 1-1 1A17 17 0 013 4c0-.6.4-1 1-1h3.5c.6 0 1 .4 1 1 0 1.3.2 2.5.6 3.6.1.3 0 .7-.2 1z"/></svg>(312) 555-0148</li>
      <li><svg width="10" height="10" viewBox="0 0 24 24"><path fill="#8cc63f" d="M3 5h18v14H3zm2 2v.5l7 4.5 7-4.5V7z"/></svg>care@vitalquorra.com</li>
      <li><svg width="10" height="10" viewBox="0 0 24 24"><path fill="#8cc63f" d="M12 2a7 7 0 00-7 7c0 5 7 13 7 13s7-8 7-13a7 7 0 00-7-7zm0 9.5A2.5 2.5 0 1112 6a2.5 2.5 0 010 5.5z"/></svg>2410 Larkmoor Avenue, Chicago, IL</li>
      <li><svg width="10" height="10" viewBox="0 0 24 24"><circle cx="12" cy="12" r="9" fill="none" stroke="#8cc63f" stroke-width="2"/></svg>www.vitalquorra.com</li>
    </ul>
  </div>
  <div class="footer-bottom">
    <ul><li>Home</li><li>Who We Are</li><li>What We Do</li><li>Services</li><li>Blog</li><li>Contact</li></ul>
  </div>
</footer>

</body>
</html>
```